Flyer for a Business Consultant

I need a one-page description of services. I am a Brinmore Accredited Talents Mentor. I do not have a personal website but think I will soon purchase this template https://quillerlayouts.example/layouts/lectern/. I like the larger font, simplicity and larger font. I will attach his pricing flyer which I like - not to overly guide or restrict your creative thinking, but only to give a little perspective. I don't like busy, noisy - I like clarity, simplicity. Here 's the Brinmore website which these same traits https://www.brinmoretalentshub.example/ and can be a source of ideas and colors.

Target Market(s)

CEOs and Middle Managers in organizations

Industry/Entity Type

Financial Service

Colors

Designer to choose colors to be used in the design.

Requirements
Must have
• Clarity, simplicity, but also strength (not weak or frilly looking)
Nice to have
• Warm color(s), larger/not skinny font
Should not have
• Loud, noisy, busy

```html
<!DOCTYPE html>
<html lang="en">
<head>
<meta charset="utf-8">
<title>Strength-Based Approach to Managing Team Effectiveness</title>
<link href="https://fonts.googleapis.com/css2?family=Oswald:wght@500;600&family=Lato:wght@400;700&display=swap" rel="stylesheet">
<style>
  :root {
    --red: #d04f38;
    --red-dark: #a5321f;
    --green: #14936b;
    --ink: #4a4a4a;
    --rule: #8c8c8c;
    --backdrop: #9a9a9a;
    --paper: #ffffff;
  }
  html, body {
    margin: 0; padding: 0;
    width: 1200px; height: 1200px;
    overflow: hidden;
    background: var(--backdrop);
  }
  .stage { position: relative; width: 1200px; height: 1200px; }
  .flyer {
    position: absolute;
    left: 193px; top: 29px;
    width: 904px; height: 1268px;
    background: var(--paper);
    transform: scale(0.9);
    transform-origin: top left;
    font-family: "Lato", sans-serif;
    color: var(--ink);
  }
  .abs { position: absolute; }

  .hero-photo {
    left: 17px; top: 81px; width: 887px; height: 453px;
    background: linear-gradient(100deg, #c9a79a 0%, #dfe3e8 45%, #8a9bb2 70%, #eef0f2 100%);
  }
  .hero-panel {
    left: 17px; top: 25px; width: 419px; height: 509px;
    background: var(--red);
    opacity: 0.93;
  }
  .hero-fold { left: 436px; top: 25px; }
  .hero-rule { left: 17px; top: 534px; }

  .headline {
    left: 42px; top: 176px; width: 380px;
    margin: 0;
    font-family: "Oswald", sans-serif;
    font-weight: 600;
    color: #fff;
    line-height: 1;
    text-transform: uppercase;
    letter-spacing: -1px;
    white-space: nowrap;
  }
  .headline span { display: block; }
  .headline .l1 { font-size: 47px; margin-bottom: 12px; }
  .headline .l2 { font-size: 63px; margin-bottom: 10px; }
  .headline .l3 { font-size: 65px; font-weight: 500; margin-bottom: 8px; }
  .headline .l4 { font-size: 55px; }
  .headline .l2 small { font-size: 40px; font-weight: 500; }
  .headline .l3 small { font-size: 42px; font-weight: 600; }

  .benefits-lead {
    left: 59px; top: 558px;
    font-weight: 700; font-size: 20px; color: var(--green);
  }
  .benefit { left: 40px; width: 380px; display: flex; align-items: flex-start; }
  .benefit svg { flex: none; }
  .benefit p {
    margin: 0 0 0 15px;
    font-size: 16px; line-height: 21.5px;
    text-align: justify;
  }
  .benefit-1 { top: 617px; }
  .benefit-2 { top: 720px; }
  .benefit-2 p { margin-top: 12px; }
  .benefit-3 { top: 813px; }
  .benefit-3 p { margin-top: 9px; }

  .divider { left: 17px; top: 917px; width: 419px; height: 2px; background: var(--rule); }

  .contact { left: 80px; top: 950px; }
  .contact .name, .contact .role {
    font-weight: 700; font-size: 20px; color: var(--green); line-height: 25px;
  }
  .contact .line { font-size: 20px; line-height: 35px; color: var(--ink); }
  .contact .email { margin-top: 7px; }

  .credential {
    left: 54px; top: 1102px; width: 345px; height: 93px;
    border: 1px solid var(--rule); box-sizing: border-box;
  }
  .credential .mark {
    position: absolute; left: 30px; top: 14px;
    width: 60px; height: 63px; background: #8e8e8e;
  }

  .service { left: 481px; width: 382px; }
  .service h2 {
    margin: 0 0 6px;
    font-family: "Oswald", sans-serif; font-weight: 600;
    font-size: 27px; line-height: 34px; letter-spacing: -0.5px;
    color: var(--red); text-transform: uppercase;
    white-space: nowrap;
  }
  .service h2 em { font-style: normal; color: var(--green); }
  .service p {
    margin: 0;
    font-size: 16px; line-height: 21.3px;
    text-align: justify;
  }
  .service p + p { margin-top: 6px; }
  .service-individual { top: 552px; }
  .service-workshop { top: 762px; }
  .service-followon { top: 994px; }

  .footer { left: 0; top: 1214px; }
  .footer-url {
    left: 0; top: 1214px; width: 715px; height: 54px;
    line-height: 52px; text-align: center;
    color: #fff; font-size: 16px;
  }
</style>
</head>
<body>
<div class="stage">
  <div class="flyer">

    <div class="abs hero-photo" role="img" aria-label="Photo of a smiling business team, a man in front holding an open laptop"></div>
    <div class="abs hero-panel"></div>
    <svg class="abs hero-fold" width="34" height="56" viewBox="0 0 34 56"><polygon points="0,0 0,56 34,56" fill="var(--red-dark)"/></svg>
    <svg class="abs hero-rule" width="419" height="18" viewBox="0 0 419 18">
      <rect x="0" y="4" width="419" height="5" fill="var(--green)"/>
      <polygon points="176,0 216,0 196,18" fill="#fff"/>
      <polygon points="182,0 210,0 196,14" fill="var(--red)"/>
    </svg>

    <h1 class="abs headline">
      <span class="l1">A Strength-Based</span>
      <span class="l2">Approach <small>to</small></span>
      <span class="l3">Managing <small>team</small></span>
      <span class="l4">Effectiveness</span>
    </h1>

    <div class="abs benefits-lead">We help teams grow stronger by:</div>

    <div class="abs benefit benefit-1">
      <svg width="70" height="70" viewBox="0 0 70 70">
        <circle cx="35" cy="35" r="33" fill="none" stroke="var(--green)" stroke-width="3"/>
        <rect x="15" y="40" width="7" height="9" fill="var(--red)"/>
        <rect x="24" y="35" width="7" height="14" fill="var(--red)"/>
        <rect x="33" y="29" width="7" height="20" fill="var(--red)"/>
        <rect x="42" y="23" width="7" height="26" fill="var(--red)"/>
        <rect x="51" y="17" width="4" height="32" fill="var(--red)"/>
      </svg>
      <p>Bringing a deep awareness of their strengths and the strengths of their associates.</p>
    </div>

    <div class="abs benefit benefit-2">
      <svg width="70" height="70" viewBox="0 0 70 70">
        <circle cx="35" cy="35" r="33" fill="none" stroke="var(--green)" stroke-width="3"/>
        <circle cx="35" cy="35" r="13" fill="none" stroke="var(--red)" stroke-width="1.5" stroke-dasharray="3 2"/>
        <circle cx="23" cy="20" r="4" fill="var(--red)"/>
        <path d="M16 31 q7 -9 14 0 z" fill="var(--red)"/>
        <circle cx="47" cy="20" r="4" fill="var(--red)"/>
        <path d="M40 31 q7 -9 14 0 z" fill="var(--red)"/>
        <circle cx="35" cy="42" r="4" fill="var(--red)"/>
        <path d="M28 53 q7 -9 14 0 z" fill="var(--red)"/>
      </svg>
      <p>Increasing the Team’s communication and sense of partnership.</p>
    </div>

    <div class="abs benefit benefit-3">
      <svg width="70" height="70" viewBox="0 0 70 70">
        <circle cx="35" cy="35" r="33" fill="none" stroke="var(--green)" stroke-width="3"/>
        <ellipse cx="35" cy="25" rx="8" ry="10" fill="var(--red)"/>
        <path d="M18 53 q2 -15 17 -16 q15 1 17 16 z" fill="var(--red)"/>
        <polygon points="33,38 37,38 36,49 34,49" fill="#fff"/>
      </svg>
      <p>Improving employee engagement and effectiveness.</p>
    </div>

    <div class="abs divider"></div>

    <div class="abs contact">
      <div class="name">Martin Ellery</div>
      <div class="role">Brinmore Workplace Talents Mentor</div>
      <div class="line email">martin@talentsgrid.example</div>
      <div class="line">555-014-2290</div>
    </div>

    <div class="abs credential" role="img" aria-label="Accreditation badge">
      <div class="mark"></div>
    </div>

    <section class="abs service service-individual">
      <h2>Individual <em>Sessions</em></h2>
      <p>Conversational feedback and coaching sessions based on Brinmore’s TalentMap assessments. These sessions last about an hour and lead to a personalized translation of the results and how their strengths show up in their work and inherent blind spots they bring.</p>
    </section>

    <section class="abs service service-workshop">
      <h2>Strength Discovery <em>Workshop</em></h2>
      <p>A retreat-style Team Workshop in which the team learns each other’s unique Top 5 strengths. The session is very interactive and provides a common language that leads to improved communication and effectiveness. Tailored in 2.3.and 4-hour options are tailored to your Team’s challenges and opportunities.</p>
    </section>

    <section class="abs service service-followon">
      <h2>Follow-on <em>Modules</em></h2>
      <p>Follow-on is important to make the insights learned to be practical and integrated into the Teams’ approach and workflows.</p>
      <p>In a debrief session included as part of the workshop, we provide several 15-minute exercise modules for use in regular meetings, and we offer guest facilitated modules of 30- 60 minutes each.</p>
    </section>

    <svg class="abs footer" width="904" height="54" viewBox="0 0 904 54">
      <polygon points="0,0 696,0 722,54 0,54" fill="var(--red)"/>
      <polygon points="696,0 904,0 904,54 722,54" fill="#fff"/>
      <polygon points="702,0 904,0 904,54 728,54" fill="var(--green)"/>
    </svg>
    <div class="abs footer-url">www.talentsgrid.example</div>

  </div>
</div>
</body>
</html>
```